Brochure Design Project for Building Designer

I need a modern and edgy brochure to introduce my new business LURO Design, Commercial and Residential Building Designers.

We specialise in Building Design, Project Management and Design Consultation.

I would like the brochure to be anywhere between 2-4 pages, depending of amount of suitable content available.
Colours to be black and white with splashes of
bright colours (mostly incorporated in photos).

Main Content of brochure to be broken up into 3 (maybe 4) sections to include:

About Us
Services
Projects

Logo Text (DESIGN etc) can be changed to white if suits better with black background.

Would be nice to include sketches to give it that architectural feel.

Samples and wording will be uploaded shortly
Updates

I HAVE PROVIDED A COMPLETE UPDATE OF PROJECT REQUIREMENTS INCLUDING ALL NEW UPLOADED FILES.

PLEASE REFER TO THE BROCHURE LAYOUT PDF UPLOADEDĀ FOR FULL INFORMATION ON PROJECT INCLUDING BROCHURE LAYOUT.

IF YOU HAVE ANY QUESTIONS OR REQUIRE ANY FURTHER INFORMATION, PLEASE LET ME KNOW

I HAVE ADDED FURTHER DEVELOPED PDF DOCUMENTS OF BROCHURE.

IF YOU HAVE TROUBLE OPENING THESE DOCS IN ADOBE ILLUSTRATOR THRU ADOBE BRIDGE PLEASE LET ME KNOW & I WILL UPLOAD AI FILES.

CAN YOU PLEASE FINE TUNE GRAPHICS AND WORK ON BACKGROUND

Target Market(s)

Builders, Property Developers, Architects, Consultants, Professionals

Industry/Entity Type

Business

Requirements
Must have
• Very Professional Look
Black and White
Simple and easy to read layout
Either A4 (if only 2 pages) or
A3 double sided with centre fold (if 4 pages)
Touch up of photos (if possible) to make them stand out of the page.
Samples of recent projects with photos
Should not have
• Any comics or similar

```html
<!DOCTYPE html>
<html lang="en">
<head>
<meta charset="utf-8">
<title>LURO Design – Brochure</title>
<link rel="stylesheet" href="https://fonts.googleapis.com/css2?family=Cabin:wght@400;600&family=Arimo:ital,wght@0,400;0,700;1,400;1,700&family=Cabin+Sketch&display=swap">
<style>
:root{
  --pink:#e8318f;
  --ink:#1f1d1e;
  --paper:#ffffff;
  --text:#333333;
  --stage:#e8e5e0;
  --red:#d8262b;
}
*{box-sizing:border-box;margin:0;padding:0}
html,body{width:1200px;height:919px;overflow:hidden}
body{background:var(--stage);position:relative;font-family:"Arimo",Arial,sans-serif;color:var(--text)}
.abs{position:absolute}
.page-label{position:absolute;font-family:"Cabin",sans-serif;font-size:24px;color:#3a3330}
.sheet{position:absolute;background:var(--paper);box-shadow:0 2px 6px rgba(0,0,0,.25)}
.sheet-outer{left:29px;top:42px;width:1143px;height:402px}
.sheet-inner{left:29px;top:501px;width:1143px;height:402px}
.fold{position:absolute;left:571px;top:0;width:1px;height:100%;background:#d6d6d6}

/* outer back */
.sketch{left:62px;top:18px;width:460px;height:262px;background:linear-gradient(170deg,#fbfbfb,#dcdcdc)}
.logo{font-family:"Cabin",sans-serif;font-weight:400;color:var(--pink);letter-spacing:6px;line-height:1}
.logo-tag{font-family:"Arimo",sans-serif;font-size:4.4px;color:#222;letter-spacing:.1px;white-space:nowrap}
.back-logo{left:224px;top:292px;font-size:54px}
.back-tag{left:226px;top:345px}
.contact{left:0;width:571px;top:362px;text-align:center;font-family:"Cabin",sans-serif;font-size:10.5px;line-height:14px;color:#333}

/* outer front */
.front{left:571px;top:0;width:572px;height:402px}
.front-band{left:0;top:0;width:572px;height:86px;background:var(--ink)}
.sectors{left:0;width:572px;top:36px;text-align:center;font-family:"Cabin",sans-serif;font-size:14.5px;color:#fff;letter-spacing:.4px;word-spacing:2px;white-space:nowrap}
.front-photo{left:0;top:86px;width:572px;height:243px;background:linear-gradient(180deg,#aac3da 0%,#5d5f66 35%,#2b2b30 70%,#8a8a86 100%)}
.front-logo{left:240px;top:336px;font-size:54px}
.front-tag{left:242px;top:388px}

/* inner left */
.inner-dark{left:0;top:0;width:260px;height:402px;background:var(--ink)}
.interior{left:13px;top:13px;width:244px;height:375px;background:linear-gradient(160deg,#cfc6b5 0%,#a99d88 45%,#3b3532 80%,#211d1c 100%)}
.tab{position:absolute;height:16px;color:#fff;font-family:"Arimo",sans-serif;font-weight:700;font-size:11px;line-height:16px;padding-left:4px;white-space:nowrap}
.tab-wide{width:133px;height:19px;line-height:19px;font-size:10px;padding-left:0;padding-right:4px;text-align:right}
.tab-rule{position:absolute;height:1px;background:#bdbdbd}
.body-text{position:absolute;font-size:7.6px;line-height:9.6px;color:#444}
.list{position:absolute;list-style:none;font-size:7.6px;color:#444;white-space:nowrap}
.list li{height:14px;line-height:14px}
.list li::before{content:"• "}
.quote-small{position:absolute;font-size:7.8px;font-style:italic;color:#333;white-space:nowrap}
.quote-small b{font-style:normal;font-size:7px}

/* inner right */
.big-quote{left:584px;top:54px;font-family:"Arimo",sans-serif;font-weight:700;font-style:italic;font-size:19.5px;line-height:23px;color:var(--pink);white-space:nowrap}
.quote-author{left:585px;top:131px;font-size:9.5px;color:#333}
.mission{left:585px;top:156px;width:254px;font-size:7.4px;line-height:9.4px;color:#444;text-align:justify}
.pool{left:584px;top:216px;width:256px;height:172px;background:linear-gradient(180deg,#0e1a22 0%,#5e4a2a 45%,#b0893f 62%,#0b3c2c 100%)}
.tile{position:absolute;width:133px;height:112px}
.tile .ph{position:absolute;left:0;top:0;width:133px;height:101px}
.tile .cap{position:absolute;left:0;bottom:0;width:133px;height:11px;background:var(--ink);color:#fff;font-size:7px;line-height:11px;text-align:center;white-space:nowrap}
.placeholder{position:absolute;left:0;top:0;width:133px;height:101px;border:1px solid #999;background:#fff;display:flex;align-items:center;justify-content:center;text-align:center;font-family:"Cabin Sketch",sans-serif;color:var(--red);font-size:18px;line-height:18px}
</style>
</head>
<body>

<div class="page-label" style="left:295px;top:14px">Back</div>
<div class="page-label" style="left:820px;top:14px">Front</div>
<div class="page-label" style="left:258px;top:469px">Front inside</div>
<div class="page-label" style="left:797px;top:469px">Back inside</div>

<!-- Outer spread -->
<section class="sheet sheet-outer">
  <div class="abs sketch" role="img" aria-label="Architectural line sketch of a multi-storey glass building"></div>
  <div class="abs logo back-logo">LURO</div>
  <div class="abs logo-tag back-tag">COMMERCIAL + RESIDENTIAL BUILDING DESIGNERS</div>
  <div class="abs contact">PO Box 418, Westbrook WA 6911 &nbsp;|&nbsp; Phone : 0400 123 987<br>Email : yourname@lurodesign.com.au &nbsp;|&nbsp; Web : www.lurodesign.com.au</div>

  <div class="abs front">
    <div class="abs front-band"></div>
    <div class="abs sectors">RESIDENTIAL &nbsp;| &nbsp;MULTI-UNIT RESIDENTIAL &nbsp;| &nbsp;COMMERCIAL &nbsp;| &nbsp;HEALTHCARE</div>
    <div class="abs front-photo" role="img" aria-label="Photo of a modern commercial office building with dark cladding and glass shopfront"></div>
    <svg class="abs" style="left:415px;top:68px" width="157" height="18" viewBox="0 0 157 18"><polygon points="14,0 157,0 157,18 0,18" fill="var(--pink)"/></svg>
    <svg class="abs" style="left:0;top:329px" width="172" height="17" viewBox="0 0 172 17"><polygon points="0,0 172,0 154,17 0,17" fill="var(--pink)"/></svg>
    <div class="abs logo front-logo">LURO</div>
    <div class="abs logo-tag front-tag">COMMERCIAL + RESIDENTIAL BUILDING DESIGNERS</div>
  </div>
</section>

<!-- Inner spread -->
<section class="sheet sheet-inner">
  <div class="abs inner-dark"></div>
  <div class="abs interior" role="img" aria-label="Photo of a double-height living and dining interior with a steel staircase"></div>

  <svg class="abs" style="left:275px;top:19px" width="92" height="16" viewBox="0 0 92 16"><polygon points="0,0 76,0 92,16 0,16" fill="var(--pink)"/></svg>
  <div class="tab" style="left:275px;top:19px">ABOUT US</div>
  <div class="tab-rule" style="left:275px;top:35px;width:288px"></div>
  <div class="body-text" style="left:278px;top:39px;width:285px">LURO design has a diverse portfolio of commercial residential work across a range of scales, budgets + project types. Areas of experience include:</div>
  <ul class="list" style="left:278px;top:59px">
    <li>COMMERCIAL DEVELOPMENTS</li>
    <li>MIXED-USE DEVELOPMENTS</li>
    <li>RESIDENTIAL &amp; MULTI RESIDENTIAL</li>
    <li>UPMARKET INDIVIDUAL HOUSES HEALTHCARE</li>
    <li>COMMERCIAL INDUSTRIAL CAFES/RESTAURANTS</li>
    <li>ALTERATIONS + ADDITIONS</li>
    <li>RESIDENTIAL COMMERCIAL INTERIOR FITOUTS</li>
  </ul>
  <div class="quote-small" style="left:330px;top:170px">"Simplicity is the ultimate sophistication" &nbsp;<b>- Lorenzo Vitale</b></div>
  <div class="body-text" style="left:278px;top:191px;width:285px">We strive to be efficient at all times in every aspect of our service + pride ourselves on our attention to detail.</div>

  <svg class="abs" style="left:275px;top:215px" width="92" height="16" viewBox="0 0 92 16"><polygon points="0,0 76,0 92,16 0,16" fill="var(--pink)"/></svg>
  <div class="tab" style="left:275px;top:215px">SERVICES</div>
  <div class="tab-rule" style="left:275px;top:231px;width:245px"></div>
  <ul class="list" style="left:278px;top:233px">
    <li>WE ARE ABLE TO PROVIDE A WIDE RANGE OF SERVICES:</li>
    <li>PROJECT PLANNING</li>
    <li>DESIGN CONCEPTS</li>
    <li>DESIGN DEVELOPMENT / DEVELOPMENT APPROVAL</li>
    <li>CONSULTANT LIAISON + MANAGEMENT BUILDING CERTIFICATION</li>
    <li>TENDER / CONSTRUCTION DOCUMENTATION</li>
    <li>PROJECT MANAGEMENT</li>
    <li>3D MODELLING &amp; RENDERS</li>
    <li>RE-DOCUMENTATION &amp; DESIGN CONSULTATION DRAFTING SERVICES</li>
  </ul>
  <div class="body-text" style="left:278px;top:364px;width:285px">We offer high quality drafting solutions for pre-designed projects of any size to ensure you get the best quality drawings for local authority + construction issue.</div>

  <div class="fold"></div>

  <div class="abs big-quote">"If design isn't<br>profitable,<br>then it's art"</div>
  <div class="abs quote-author">-Henrik Falster</div>
  <div class="abs mission">Each project is unique, requiring a unique solution. Our aim is to provide a cost effective + sustainable design that is appropriate + responsive to our clients needs.<br><br>We believe "good design need not be expensive</div>
  <div class="abs pool" role="img" aria-label="Night photo of a house interior opening onto a lit swimming pool"></div>

  <div class="tab-rule" style="left:851px;top:38px;width:172px"></div>
  <svg class="abs" style="left:995px;top:13px" width="133" height="19" viewBox="0 0 133 19"><polygon points="14,0 133,0 133,19 0,19" fill="var(--pink)"/></svg>
  <div class="tab tab-wide" style="left:995px;top:13px">PROJECT EXPERIENCE</div>

  <div class="tile" style="left:851px;top:44px"><div class="ph" role="img" aria-label="Photo of a commercial office building" style="background:linear-gradient(180deg,#b9cde0,#3a3b40 55%,#b6b4ad)"></div><div class="cap">COMMERCIAL</div></div>
  <div class="tile" style="left:995px;top:44px"><div class="ph" role="img" aria-label="Photo of a healthcare building on a street corner" style="background:linear-gradient(180deg,#d8e3ec,#e4e2de 50%,#8f8b86)"></div><div class="cap">HEALTHCARE</div></div>
  <div class="tile" style="left:851px;top:160px"><div class="ph" role="img" aria-label="Photo of a multi-residential apartment block with a pool" style="background:linear-gradient(180deg,#6f9fd0,#d9c7b0 50%,#4a9fb4)"></div><div class="cap">MULTI-RESIDENTIAL + MIXED USE</div></div>
  <div class="tile" style="left:995px;top:160px"><div class="ph" role="img" aria-label="Photo of a modern white residential house" style="background:linear-gradient(180deg,#7aa8d6,#eef0ef 55%,#9fb2a6)"></div><div class="cap">RESIDENTIAL</div></div>
  <div class="tile" style="left:851px;top:276px"><div class="ph" role="img" aria-label="Night photo of a cafe and restaurant frontage under trees" style="background:linear-gradient(180deg,#0d1a12,#2f4a2a 50%,#a8323a)"></div><div class="cap">CAFE / RESTAURANT</div></div>
  <div class="tile" style="left:995px;top:276px"><div class="placeholder">PHOTO<br>TO BE<br>CONFIRMED</div><div class="cap">ALTERATIONS + ADDITIONS</div></div>
</section>

</body>
</html>
```